International Trading Company, 'KIRO' needs a Business Card

The company name is "KIRO" and it has own logo design.
I'd like to use its logo on this business card.
I need two side Business Card.
I'll look forward to your great design.
Thank you very much in advance.

Contact Information for Business Card

Company Name : Kiro Harbour Limited
Information Example
Dorian Pallister
Mobile(use icon please) : 1 (212) 555-0143
Tel(use icon please) : 1 (212) 555-0178
Email(use icon please) : dorian27@kiroharbour-mail.com
Address(use icon please) : 482 Halden Ave, New York, NY 10160, USA

```html
<!DOCTYPE html>
<html lang="en">
<head>
<meta charset="utf-8">
<title>Kiro Harbour Limited – Business Card</title>
<link rel="stylesheet" href="https://fonts.googleapis.com/css2?family=Open+Sans:wght@400;600&display=swap">
<style>
  :root {
    --page: #ffffff;
    --metal-dark: #b9babd;
    --metal-mid: #cfd0d3;
    --metal-light: #ebecee;
    --brush-line: rgba(255,255,255,0.18);
    --brush-shade: rgba(120,122,128,0.08);
    --ink: #1c1c1e;
    --logo-grey: #56575a;
    --sub-grey: #8a8b8e;
    --band: #141416;
    --band-text: #ffffff;
    --band-sub: #d8d8da;
  }
  * { box-sizing: border-box; margin: 0; padding: 0; }
  html, body {
    width: 1200px; height: 1200px; overflow: hidden;
    background: var(--page);
    font-family: "Open Sans", Arial, sans-serif;
  }
  .canvas { position: relative; width: 1200px; height: 1200px; }

  .card {
    position: absolute;
    left: 178px;
    width: 845px;
    height: 493px;
    overflow: hidden;
    background:
      repeating-linear-gradient(180deg, var(--brush-line) 0 1px, transparent 1px 3px, var(--brush-shade) 3px 4px, transparent 4px 6px),
      linear-gradient(90deg, var(--metal-dark) 0%, var(--metal-mid) 25%, var(--metal-light) 50%, var(--metal-mid) 68%, var(--metal-dark) 100%);
    box-shadow: 0 14px 24px rgba(0,0,0,0.18);
  }
  .card--front { top: 55px; }
  .card--back { top: 596px; }

  .brand {
    position: absolute; left: 0; right: 0; top: 228px;
    text-align: center;
  }
  .brand__mark {
    position: absolute; left: 0; right: 0; top: -108px;
    font-weight: 600; font-size: 58px; line-height: 1;
    letter-spacing: 3px; color: var(--logo-grey);
  }
  .brand__name {
    font-weight: 400; font-size: 50px; line-height: 1.1; color: var(--ink);
  }
  .brand__tagline {
    font-weight: 400; font-size: 26px; line-height: 1.2; color: var(--sub-grey);
  }

  .name-band {
    position: absolute; left: 0; top: 174px;
    width: 414px; height: 146px;
    background: var(--band);
    text-align: center;
    padding-top: 24px;
  }
  .name-band__name {
    font-size: 54px; line-height: 1.1; color: var(--band-text); font-weight: 400;
  }
  .name-band__role {
    font-size: 21px; color: var(--band-sub); margin-top: 6px;
  }

  .contact {
    position: absolute; left: 490px;
    display: flex; align-items: center; gap: 22px;
  }
  .contact__icon {
    width: 56px; height: 56px; border-radius: 8px;
    background: var(--band);
    display: flex; align-items: center; justify-content: center;
    flex: none;
  }
  .contact__icon svg { width: 26px; height: 26px; fill: #ffffff; }
  .contact__text { font-size: 16.5px; line-height: 1.6; color: var(--ink); }
  .contact--address { top: 112px; }
  .contact--email { top: 220px; }
  .contact--phone { top: 326px; }
</style>
</head>
<body>
<main class="canvas">
  <section class="card card--front">
    <div class="brand">
      <div class="brand__mark">KIRO</div>
      <div class="brand__name">Kiro Harbour Limited</div>
      <div class="brand__tagline">International Trading Company</div>
    </div>
  </section>

  <section class="card card--back">
    <div class="name-band">
      <div class="name-band__name">Dorian Pallister</div>
      <div class="name-band__role">General Manager</div>
    </div>

    <div class="contact contact--address">
      <div class="contact__icon">
        <svg viewBox="0 0 24 24" aria-hidden="true"><path d="M12 2a7 7 0 0 0-7 7c0 5 7 13 7 13s7-8 7-13a7 7 0 0 0-7-7zm0 9.5A2.5 2.5 0 1 1 12 6.5a2.5 2.5 0 0 1 0 5z"/></svg>
      </div>
      <div class="contact__text">482 Halden Ave, New York,<br>NY 10160, USA</div>
    </div>

    <div class="contact contact--email">
      <div class="contact__icon">
        <svg viewBox="0 0 24 24" aria-hidden="true"><path d="M3 6h18v12H3z" fill="none" stroke="#fff" stroke-width="1.8"/><path d="M3 6l9 7 9-7" fill="none" stroke="#fff" stroke-width="1.8"/></svg>
      </div>
      <div class="contact__text">dorian27@kiroharbour-mail.com</div>
    </div>

    <div class="contact contact--phone">
      <div class="contact__icon">
        <svg viewBox="0 0 24 24" aria-hidden="true"><path d="M6.6 10.8a15.1 15.1 0 0 0 6.6 6.6l2.2-2.2a1 1 0 0 1 1-.25 11.4 11.4 0 0 0 3.6.57 1 1 0 0 1 1 1V20a1 1 0 0 1-1 1A17 17 0 0 1 3 4a1 1 0 0 1 1-1h3.5a1 1 0 0 1 1 1c0 1.25.2 2.45.57 3.57a1 1 0 0 1-.25 1z"/></svg>
      </div>
      <div class="contact__text">1 (212) 555-0178<br>1 (212) 555-0143</div>
    </div>
  </section>
</main>
</body>
</html>
```